Oil and Gas Letterhead Design Tweak

Simple letterhead information and design tweak.

Please note, we don't want to change the design or logo of the letterhead only the small changes mentioned below.

We need to change the company name up top to "Northvale Petrotek FZCO"

Also, we need to include in the footer the following information. I have attached an image of roughly how we would like to have it displayed in the footer.

Footer Details:

Northvale Petrotek FZCO,
Unit No. 2378, FZCO Trade Hub, level No. 1, K&P 7, Dubai, United Arab Emirates
Northvale Petrotek FZCO is registered as a free zone company under the rules & regulations of FZCO

Target Market(s)

O&G Market

Industry/Entity Type

Oil And Gas

Font styles to use
Sans Serif

Colors

Designer to choose colors to be used in the design.

Requirements
Must have
• Change the company name to Northvale Petrotek FZCO
• Include the footer on the bottom of the first and continuation page
Should not have
• Should not change the design or logo of the letterhead, only the specified changes mentioned above

```html
<!DOCTYPE html>
<html lang="en">
<head>
<meta charset="utf-8">
<title>Northvale Petrotek FZCO — Letterhead</title>
<link rel="stylesheet" href="https://fonts.googleapis.com/css2?family=Jost:wght@400;500;600&display=swap">
<style>
  :root {
    --brand-blue: #1f4f9f;
    --brand-red: #e3262e;
    --ink: #1c1c1c;
    --paper: #ffffff;
    --backdrop: #e6e6e6;
    --shadow: rgba(0, 0, 0, 0.12);
  }
  * { box-sizing: border-box; margin: 0; padding: 0; }
  html, body {
    width: 1200px; height: 800px; overflow: hidden;
    background: var(--backdrop);
    font-family: "Jost", "Futura", sans-serif;
    color: var(--ink);
  }
  .stationery { position: relative; width: 1200px; height: 800px; }
  .sheet {
    position: absolute; top: 50px;
    width: 495px; height: 700px;
    background: var(--paper);
    box-shadow: 0 4px 18px var(--shadow);
    overflow: hidden;
  }
  .sheet--first { left: 70px; }
  .sheet--continuation { left: 635px; }

  .stripe { position: absolute; display: block; }
  .stripe--top { top: 0; left: 0; width: 495px; height: 18px; }
  .stripe--corner-top { top: 0; right: 0; width: 130px; height: 14px; }
  .stripe--bottom { bottom: 0; left: 0; width: 495px; height: 14px; }
  .stripe--corner-bottom { bottom: 0; right: 0; width: 130px; height: 14px; }

  .masthead {
    position: absolute; top: 34px; left: 36px;
    display: flex; align-items: center; gap: 10px;
  }
  .masthead__mark { width: 14px; height: 14px; background: var(--brand-red); }
  .masthead__name {
    font-size: 15px; font-weight: 500; letter-spacing: 0.04em;
    text-transform: uppercase; color: var(--ink);
  }

  .footer {
    position: absolute; left: 12px; right: 12px; bottom: 22px;
    display: flex; justify-content: space-between; align-items: flex-end;
  }
  .footer__details { font-size: 6.4px; line-height: 1.3; letter-spacing: 0.02em; }
  .footer__company { font-weight: 600; font-size: 7.2px; text-transform: uppercase; }
  .footer__badge {
    display: flex; flex-direction: column; align-items: center; gap: 3px;
    width: 76px; margin-right: 30px;
  }
  .footer__badge-mark { width: 12px; height: 12px; background: var(--brand-red); }
  .footer__badge-name {
    font-size: 6px; font-weight: 500; text-transform: uppercase;
    text-align: center; line-height: 1.2;
  }
</style>
</head>
<body>
<main class="stationery">

  <section class="sheet sheet--first" aria-label="First page letterhead">
    <svg class="stripe stripe--top" viewBox="0 0 495 18" aria-hidden="true">
      <polygon points="0,8 205,8 196,16 0,16" fill="var(--brand-blue)"/>
      <polygon points="222,0 495,0 495,8 213,8" fill="var(--brand-red)"/>
    </svg>
    <header class="masthead">
      <span class="masthead__mark" aria-hidden="true"></span>
      <h1 class="masthead__name">Northvale Petrotek FZCO</h1>
    </header>
    <footer class="footer">
      <div class="footer__details">
        <p class="footer__company">Northvale Petrotek FZCO</p>
        <p>Unit No. 2378 | FZCO Trade Hub | level No. 1, K&amp;P 7 | Dubai | United Arab Emirates</p>
        <p>Northvale Petrotek FZCO is registered as a free zone company under the rules &amp; regulations of FZCO</p>
      </div>
    </footer>
    <svg class="stripe stripe--corner-bottom" viewBox="0 0 130 14" aria-hidden="true">
      <polygon points="12,14 60,14 68,6 20,6" fill="var(--brand-blue)"/>
      <polygon points="70,14 130,14 130,4 80,4" fill="var(--brand-red)"/>
    </svg>
  </section>

  <section class="sheet sheet--continuation" aria-label="Continuation page letterhead">
    <svg class="stripe stripe--corner-top" viewBox="0 0 130 14" aria-hidden="true">
      <polygon points="0,0 40,0 32,10 8,10" fill="var(--brand-blue)"/>
      <polygon points="52,0 90,0 80,10 42,10" fill="var(--brand-red)"/>
    </svg>
    <footer class="footer">
      <div class="footer__details">
        <p class="footer__company">Northvale Petrotek FZCO</p>
        <p>Unit No. 2378 | FZCO Trade Hub | level No. 1, K&amp;P 7 | Dubai | United Arab Emirates</p>
        <p>Northvale Petrotek FZCO is registered as a free zone company under the rules &amp; regulations of FZCO</p>
      </div>
      <div class="footer__badge">
        <span class="footer__badge-mark" aria-hidden="true"></span>
        <span class="footer__badge-name">Northvale<br>Petrotek FZCO</span>
      </div>
    </footer>
    <svg class="stripe stripe--bottom" viewBox="0 0 495 14" aria-hidden="true">
      <polygon points="0,6 390,6 386,10 0,10" fill="var(--brand-blue)"/>
      <polygon points="436,6 495,6 495,14 440,14" fill="var(--brand-red)"/>
    </svg>
  </section>

</main>
</body>
</html>
```